Webpage Design Layout for Thanksgiving/App Charity

Hi,

I am putting together a website called http://kindlyloop.example with the intention of getting app developers to giveaway their usual thanksgiving discount to a charity rather than to the customer.

I am looking for a one page design (not coded) that will have;

1. A header and small description of the idea. For example;

"KindlyLoop - Sharing Makes Ripples"

KindlyLoop is a movement that lets developers and users pass on the usual Thanksgiving discounts to people and communities who need it most. Buy your favourite apps from the links below and 40% of the price goes directly to charity"

2. A small section outlining the charity (not yet selected) with a link to learn more and a 'Play Video' button. I'd like to include a video of the charity.

3. A grid showing the available apps with an 'About' button and 'Buy Now' button

4. a FAQ underneath the apps

5. Some kind of prominent "Money raised" bar that will go near the top of the page

6. A footer section with contact info, mailing list sign up.

7. A countdown timer near the top that will countdown until the charity is over

8. A logo that would represent Apps + Thanksgiving

Obviously since this ties in with thanksgiving and apps I'd like to make it a fun turkey or thanksgiving themed page.

Please use Google Fonts and make sure to have the rights to any images used.

Target Market(s)

I want to appeal to every day phone and computer users. It should be a fun page but that also display credibility and confidence for purchasers/visitors.

Industry/Entity Type

Software

Number of Pages Required

1 page

Requirements
Must have
• Just a fun page that displays credibility and the importance of the idea

```html
<!DOCTYPE html>
<html lang="en">
<head>
<meta charset="utf-8">
<title>KindlyLoop - Sharing Makes Ripples</title>
<link rel="stylesheet" href="https://fonts.googleapis.com/css2?family=Raleway:wght@500;600;700;800&family=Open+Sans:wght@400;600;700&display=swap">
<style>
:root{
  --blue:#0aa2da;
  --orange:#f37a2c;
  --ink:#2b2b2b;
  --muted:#666;
  --light:#f6f6f6;
  --line:#e4e4e4;
  --white:#fff;
  --timer:#3c3c3c;
}
*{margin:0;padding:0;box-sizing:border-box}
html,body{width:1200px;height:2727px;overflow:hidden}
body{font-family:"Open Sans",Arial,sans-serif;color:var(--ink);background:var(--white);position:relative}
.abs{position:absolute}
.center{left:0;width:1200px;text-align:center}
h1,h2,h3{font-family:"Raleway",Arial,sans-serif}

/* header */
.site-header{position:absolute;top:0;left:0;width:1200px;height:116px;background:var(--white)}
.brand{position:absolute;left:149px;top:30px;display:flex;align-items:center;gap:16px}
.brand-mark{width:52px;height:52px;border-radius:10px;background:var(--orange)}
.brand-name{font-family:"Raleway",Arial,sans-serif;font-weight:800;font-size:31px;color:var(--ink);letter-spacing:.5px}
.main-nav a{position:absolute;top:50px;font-family:"Raleway",Arial,sans-serif;font-weight:700;font-size:13px;color:var(--ink);text-decoration:none;letter-spacing:.3px}
.main-nav a.active{color:var(--blue)}

/* hero */
.hero{position:absolute;top:116px;left:0;width:1200px;height:534px;overflow:hidden}
.hero-photo{position:absolute;inset:0;background:linear-gradient(100deg,#3b3630 0%,#26221e 40%,#1f1d1b 70%,#3a3c3e 100%)}
.hero-shade{position:absolute;inset:0;background:rgba(0,0,0,.35)}
.countdown{position:absolute;left:855px;top:0;width:209px;height:57px;background:var(--white);border-radius:0 0 30px 30px;display:flex;justify-content:center;gap:8px;padding-top:3px}
.countdown .unit{text-align:center}
.countdown .num{display:block;width:38px;height:30px;background:var(--timer);color:var(--white);font-weight:700;font-size:18px;line-height:30px;border-radius:3px}
.countdown .lbl{font-size:9px;color:var(--muted)}
.hero-kicker{top:88px;font-weight:800;font-size:27px;color:var(--white);letter-spacing:1px}
.hero-title{top:126px;font-weight:800;font-size:64px;color:var(--white);letter-spacing:1px}
.hero-sub{top:212px;font-family:"Raleway",Arial,sans-serif;font-weight:700;font-size:22px;color:var(--blue);letter-spacing:.5px}
.hero-text{top:254px;left:260px;width:680px;text-align:center;font-size:15px;line-height:30px;color:var(--white)}
.raise-bar{position:absolute;left:267px;top:379px;width:664px;height:26px;border-radius:13px;background:var(--white);border:3px solid var(--orange)}
.raise-fill{position:absolute;left:0;top:0;height:100%;width:352px;background:var(--orange);border-radius:10px 0 0 10px}
.knob{position:absolute;top:-10px;width:40px;height:40px;border-radius:50%;border:5px solid var(--white)}
.knob.raised{left:331px;background:var(--orange)}
.knob.goal{right:-14px;background:var(--blue)}
.raise-label{top:424px;font-family:"Raleway",Arial,sans-serif;font-weight:600;font-size:15px;color:var(--white)}
.raise-value{top:454px;font-family:"Raleway",Arial,sans-serif;font-weight:700;font-size:17px;color:var(--white)}

/* charity */
.charity{position:absolute;top:650px;left:0;width:1200px;height:679px;background:linear-gradient(135deg,#0ba6de,#0a97cf)}
.charity h2{top:52px;font-weight:800;font-size:30px;color:var(--white);letter-spacing:.5px}
.charity .lede{top:98px;font-family:"Raleway",Arial,sans-serif;font-weight:600;font-size:18px;color:var(--white)}
.video{position:absolute;left:238px;top:177px;width:724px;height:348px;border:8px solid var(--white);box-shadow:0 4px 14px rgba(0,0,0,.2)}
.video-still{position:absolute;inset:0;background:linear-gradient(180deg,#7b8f6a 0%,#6b7e5a 55%,#4f6a3c 100%)}
.play{position:absolute;left:314px;top:118px}
.btn-solid{position:absolute;left:529px;top:557px;width:142px;height:46px;border-radius:23px;background:var(--orange);color:var(--white);font-family:"Raleway",Arial,sans-serif;font-weight:700;font-size:13px;line-height:46px;text-align:center}

/* apps */
.apps{position:absolute;top:1329px;left:0;width:1200px;height:838px;background:var(--light)}
.apps h2{top:62px;font-weight:800;font-size:30px;color:var(--ink);letter-spacing:.5px}
.app-card{position:absolute;width:443px;height:215px;background:var(--white);border:1px solid var(--line)}
.app-icon{position:absolute;left:153px;top:-68px;width:136px;height:136px;border-radius:50%;background:var(--white);border:1px solid var(--line);display:flex;align-items:center;justify-content:center}
.app-art{width:72px;height:72px;border-radius:12px}
.app-desc{position:absolute;left:40px;top:88px;width:363px;text-align:center;font-size:11.5px;line-height:25px;color:var(--muted)}
.app-btn{position:absolute;top:154px;width:102px;height:32px;border-radius:16px;font-family:"Raleway",Arial,sans-serif;font-weight:700;font-size:11px;line-height:30px;text-align:center;background:var(--white)}
.app-btn.more{left:116px;border:1.5px solid var(--orange);color:var(--orange)}
.app-btn.buy{left:225px;border:1.5px solid var(--blue);color:var(--blue)}

/* faq */
.faq{position:absolute;top:2167px;left:0;width:1200px;height:242px;background:var(--orange);color:var(--white)}
.faq h2{top:44px;font-weight:800;font-size:30px}
.faq-item{position:absolute;top:108px;width:440px}
.faq-item h3{font-weight:700;font-size:16px;margin-bottom:10px}
.faq-item p{font-size:12px;line-height:21px}
.faq-divider{position:absolute;left:600px;top:110px;width:1px;height:80px;background:rgba(255,255,255,.4)}

/* footer */
.site-footer{position:absolute;top:2409px;left:0;width:1200px;height:318px;background:var(--white)}
.foot-col{position:absolute;top:42px}
.foot-col h3{font-weight:600;font-size:18px;color:var(--ink);margin-bottom:16px}
.foot-col li{list-style:none;font-size:12px;line-height:23px;color:var(--muted)}
.foot-col p{font-size:12px;line-height:20px;color:var(--muted)}
.email-field{margin-top:14px;width:240px;height:36px;border:1px solid #ccc;font-size:11px;color:#aaa;line-height:34px;padding-left:14px}
.subscribe{margin-top:12px;width:106px;height:34px;border-radius:17px;background:var(--orange);color:var(--white);font-family:"Raleway",Arial,sans-serif;font-weight:700;font-size:11px;line-height:34px;text-align:center}
.contact-row{display:flex;gap:18px;font-size:12px;line-height:20px;color:var(--muted);margin-bottom:22px}
.contact-row svg{flex:none;margin-top:3px}
.social-row{display:flex;align-items:center;gap:14px;font-size:12px;color:var(--muted);margin-bottom:8px}
.social-dot{width:26px;height:26px;border-radius:50%;border:1.5px solid var(--blue)}
.foot-rule{position:absolute;left:131px;top:247px;width:968px;height:1px;background:var(--line)}
.copyright{top:272px;font-size:11.5px;color:var(--muted)}
</style>
</head>
<body>

<header class="site-header">
  <div class="brand"><span class="brand-mark"></span><span class="brand-name">KINDLYLOOP</span></div>
  <nav class="main-nav">
    <a class="active" style="left:567px">HOME</a>
    <a style="left:655px">ABOUT</a>
    <a style="left:747px">CHARITY</a>
    <a style="left:849px">APPS</a>
    <a style="left:930px">FAQ</a>
    <a style="left:1005px">CONTACT</a>
  </nav>
</header>

<section class="hero">
  <div class="hero-photo" role="img" aria-label="Photo of a smiling woman using a tablet at a cafe table"></div>
  <div class="hero-shade"></div>
  <div class="countdown">
    <div class="unit"><span class="num">05</span><span class="lbl">Hour</span></div>
    <div class="unit"><span class="num">24</span><span class="lbl">Minute</span></div>
    <div class="unit"><span class="num">36</span><span class="lbl">Second</span></div>
  </div>
  <h3 class="abs center hero-kicker">KINDLYLOOP:</h3>
  <h1 class="abs center hero-title">SHARING MAKES RIPPLES</h1>
  <p class="abs center hero-sub">40% OF ALL PURCHASES GOES TO CHARITY</p>
  <p class="abs hero-text">KindlyLoop is a movement that lets developers and users pass on the usual Thanksgiving discounts to people and communities who need it most. Buy your favourite apps from the links below and 40% of the price goes directly to charity"</p>
  <div class="raise-bar"><div class="raise-fill"></div><span class="knob raised"></span><span class="knob goal"></span></div>
  <span class="abs raise-label" style="left:267px">Money Raised</span>
  <span class="abs raise-label" style="left:899px">Goal</span>
  <span class="abs raise-value" style="left:267px">$ 500</span>
  <span class="abs raise-value" style="left:870px">$50,000</span>
</section>

<section class="charity">
  <h2 class="abs center">CHARITY KINDLYLOOP</h2>
  <p class="abs center lede">Charity KindlyLoop helps children develop the skills they need......</p>
  <div class="video">
    <div class="video-still" role="img" aria-label="Video still of happy children running across a grassy park"></div>
    <svg class="play" width="96" height="96" viewBox="0 0 96 96"><circle cx="48" cy="48" r="44" fill="rgba(0,0,0,.15)" stroke="#fff" stroke-width="5"/><path d="M38 28 L68 48 L38 68 Z" fill="#fff"/></svg>
  </div>
  <div class="btn-solid">LEARN MORE</div>
</section>

<section class="apps">
  <h2 class="abs center">AVAILABLE APPS</h2>

  <article class="app-card" style="left:133px;top:207px">
    <div class="app-icon"><span class="app-art" role="img" aria-label="App store icon" style="background:linear-gradient(135deg,#3cc7d6,#f2c94c)"></span></div>
    <p class="app-desc">PageCraft is an easy to use website builder for DeskOS. The visual website builder is easy to use....</p>
    <span class="app-btn more">LEARN MORE</span><span class="app-btn buy">BUY NOW</span>
  </article>

  <article class="app-card" style="left:624px;top:207px">
    <div class="app-icon"><span class="app-art" role="img" aria-label="App grid icon" style="background:linear-gradient(135deg,#f2c94c,#7ba7e0 50%,#e05a4a)"></span></div>
    <p class="app-desc">PageCraft is an easy to use website builder for DeskOS. The visual website builder is easy to use....</p>
    <span class="app-btn more">LEARN MORE</span><span class="app-btn buy">BUY NOW</span>
  </article>

  <article class="app-card" style="left:133px;top:527px">
    <div class="app-icon"><span class="app-art" role="img" aria-label="Hand holding a phone illustration" style="background:linear-gradient(135deg,#f0a35e,#e85c4a)"></span></div>
    <p class="app-desc">PageCraft is an easy to use website builder for DeskOS. The visual website builder is easy to use....</p>
    <span class="app-btn more">LEARN MORE</span><span class="app-btn buy">BUY NOW</span>
  </article>

  <article class="app-card" style="left:624px;top:527px">
    <div class="app-icon"><span class="app-art" role="img" aria-label="Smartphone with app icons illustration" style="background:linear-gradient(180deg,#5a6675,#3f4a57);width:44px"></span></div>
    <p class="app-desc">PageCraft is an easy to use website builder for DeskOS. The visual website builder is easy to use....</p>
    <span class="app-btn more">LEARN MORE</span><span class="app-btn buy">BUY NOW</span>
  </article>
</section>

<section class="faq">
  <h2 class="abs center">FAQ'S</h2>
  <div class="faq-item" style="left:131px">
    <h3>How much money goes charity?</h3>
    <p>40% off all purchases that go through the Buy Now button for each app goes to charity</p>
  </div>
  <div class="faq-divider"></div>
  <div class="faq-item" style="left:675px">
    <h3>What Charity will the money go to?</h3>
    <p>40% off all purchases that go through the Buy Now button for each app goes to charity</p>
  </div>
</section>

<footer class="site-footer">
  <div class="foot-col" style="left:131px">
    <h3>Quick Links</h3>
    <ul><li>Home</li><li>About</li><li>Charity Apps</li><li>FAQ</li><li>Contact</li></ul>
  </div>
  <div class="foot-col" style="left:338px">
    <h3>Newsletter Subscription</h3>
    <p>Register your Email Address to get<br>Information about us</p>
    <div class="email-field">Email Address</div>
    <div class="subscribe">SUBSCRIBE</div>
  </div>
  <div class="foot-col" style="left:700px">
    <h3>Contact Us</h3>
    <div class="contact-row"><svg width="10" height="14" viewBox="0 0 10 14"><path d="M5 0a5 5 0 0 1 5 5c0 4-5 9-5 9S0 9 0 5a5 5 0 0 1 5-5z" fill="#0aa2da"/><circle cx="5" cy="5" r="1.8" fill="#fff"/></svg><span>Box 51207 kindlyloop<br>Maple Lane, City-210</span></div>
    <div class="contact-row"><svg width="12" height="12" viewBox="0 0 12 12"><path d="M2 0l3 3-1.5 1.5a8 8 0 0 0 4 4L9 7l3 3-2 2C5 12 0 7 0 2z" fill="#0aa2da"/></svg><span>1 555 010 2040</span></div>
    <div class="contact-row"><svg width="13" height="10" viewBox="0 0 13 10"><rect width="13" height="10" rx="1" fill="#0aa2da"/><path d="M0 1l6.5 5L13 1" stroke="#fff" fill="none"/></svg><span>info@kindlyloop.example</span></div>
  </div>
  <div class="foot-col" style="left:971px">
    <h3>Follow Us</h3>
    <div class="social-row"><span class="social-dot"></span>Circlefeed</div>
    <div class="social-row"><span class="social-dot"></span>Chirper</div>
    <div class="social-row"><span class="social-dot"></span>Orbitplus</div>
    <div class="social-row"><span class="social-dot"></span>Viewtube</div>
  </div>
  <div class="foot-rule"></div>
  <p class="abs center copyright">Copyright © 2017, kindlyloop. All rights reserved.</p>
</footer>

</body>
</html>
```